Men’s hair skin and beard line

I own a men’s salon in Texas and are beginning to expand its market into the men’s retail line and already have it being manufactured out of the UK. It’s paraben free, vegan, sulphate free. I need a better brand look for the packaging. This script font is a bit hard to read. I want it masculine yet clean lines. All colors even gold or silver are welcomed. Bottle choices are silver canisters, white or black.

Target Market(s)

Men

Industry/Entity Type

Men’s hair skin and beard industry. Retail centers, high end barbers, and gyms

Font styles to use
Other font styles liked:
• Montserrat ,helvetica neue, or lato font

Colors
0054AA
0677BA
7BADD7
CADEEF
E8F1F8
0094D4
00A9DD
6FCCEA
C7EBF8
E9F6FB
00AB8E
00BBA5
67D7C9
C6EFE9
E9F9F6

Requirements
Must have
• Logo and name
Nice to have
• I’m open to all.
Should not have
• Not feminine

```html
<!DOCTYPE html>
<html lang="en">
<head>
<meta charset="UTF-8">
<title>Ironvale Signature Line – Shaving Gel Labels</title>
<link href="https://fonts.googleapis.com/css2?family=Montserrat:wght@300;400;600&display=swap" rel="stylesheet">
<style>
  :root {
    --canvas: #ffffff;
    --gold: #8a7536;
    --label-white: #ffffff;
    --label-white-edge: #e6e6e6;
    --label-black: #050505;
    --label-black-soft: #2a2a2a;
    --ink-dark: #2b2b2b;
    --ink-light: #b8b8b8;
  }
  * { margin: 0; padding: 0; box-sizing: border-box; }
  html, body {
    width: 1200px; height: 983px; overflow: hidden;
    background: var(--canvas);
    font-family: "Montserrat", sans-serif;
  }
  .stage { position: relative; width: 1200px; height: 983px; }

  .label {
    position: absolute;
    top: 268px;
    width: 236px;
    height: 578px;
    border-radius: 22px;
  }
  .label--white {
    left: 310px;
    background: var(--label-white);
    border: 1px solid var(--label-white-edge);
    box-shadow: 0 10px 24px rgba(0,0,0,0.06);
  }
  .label--black {
    left: 662px;
    background: radial-gradient(ellipse at 50% 95%, var(--label-black-soft) 0%, var(--label-black) 45%);
  }

  .brand {
    position: absolute;
    top: 52px; left: 0; right: 0;
    text-align: center;
    color: var(--gold);
  }
  .brand__name {
    display: inline-flex; align-items: center; gap: 7px;
    font-weight: 600; font-size: 19px; letter-spacing: 1.5px;
    text-transform: uppercase;
  }
  .brand__mark { width: 15px; height: 15px; background: var(--gold); }
  .brand__line {
    display: block;
    font-weight: 400; font-size: 7px; letter-spacing: 3px;
    margin-top: 2px; padding-left: 20px;
  }

  .vertical {
    position: absolute;
    bottom: 92px;
    writing-mode: vertical-rl;
    transform: rotate(180deg);
    white-space: nowrap;
  }
  .product-name {
    left: 20px;
    font-weight: 300; font-size: 50px; letter-spacing: 5px;
    color: var(--gold); line-height: 1;
  }
  .product-type {
    left: 66px;
    font-weight: 400; font-size: 17px; letter-spacing: 0.5px;
    line-height: 1;
  }
  .label--white .product-type { color: var(--ink-dark); }
  .label--black .product-type { color: var(--ink-light); }

  .directions {
    position: absolute;
    top: 442px; right: 9px;
    width: 150px;
    text-align: right;
    font-size: 6.5px; line-height: 1.15;
  }
  .label--white .directions { color: var(--ink-dark); }
  .label--black .directions { color: var(--ink-light); }

  .volume {
    position: absolute;
    top: 517px; left: 0; right: 0;
    text-align: center;
    font-weight: 400; font-size: 16px; letter-spacing: -0.3px;
  }
  .label--white .volume { color: var(--ink-dark); }
  .label--black .volume { color: var(--ink-light); }
</style>
</head>
<body>
<main class="stage">
  <section class="label label--white">
    <div class="brand">
      <span class="brand__name"><span class="brand__mark"></span>Ironvale</span>
      <span class="brand__line">SIGNATURE LINE</span>
    </div>
    <h1 class="vertical product-name">SHARING GEL</h1>
    <p class="vertical product-type">Pre Shave Softening Gel</p>
    <p class="directions">When gel is applied<br>by massaging,it will rapidly soften<br>the beard, ensuring the shaving blade<br>can easily glide and thus prevent<br>irritation of the skin</p>
    <p class="volume">250ml / 8.4fl.oz</p>
  </section>

  <section class="label label--black">
    <div class="brand">
      <span class="brand__name"><span class="brand__mark"></span>Ironvale</span>
      <span class="brand__line">SIGNATURE LINE</span>
    </div>
    <h2 class="vertical product-name">SHARING GEL</h2>
    <p class="vertical product-type">Pre Shave Softening Gel</p>
    <p class="directions">When gel is applied<br>by massaging,it will rapidly soften<br>the beard, ensuring the shaving blade<br>can easily glide and thus prevent<br>irritation of the skin</p>
    <p class="volume">250ml / 8.4fl.oz</p>
  </section>
</main>
</body>
</html>
```